Eye Catching Wrap for Keystone Plumbing

We would like a truck wrap (box truck/transit) that is distinguishable, unique, and eye catching. Stick with the basic colors within the logo but feel free to add more as long as it’s not over done. Must include the following:
-phone number (big and bold 555-872-3096)
-logo
-“Keystone Quality Guaranteed” (or your own slogan if it’s better
-military and first responder discounts
-website

```html
<!DOCTYPE html>
<html lang="en">
<head>
<meta charset="UTF-8">
<title>Keystone Plumbing Truck Wrap</title>
<link href="https://fonts.googleapis.com/css2?family=Montserrat:wght@600;700;800&display=swap" rel="stylesheet">
<style>
  :root {
    --blue: #1f5bb0;
    --orange: #ec5a1e;
    --teal: #2bb3c9;
    --white: #ffffff;
    --off-white: #eef1f4;
    --ground: #d9d6cf;
  }
  * { margin: 0; padding: 0; box-sizing: border-box; }
  html, body { width: 1200px; height: 1200px; overflow: hidden; }
  body {
    background: var(--ground);
    font-family: "Montserrat", sans-serif;
    position: relative;
  }
  .panel { position: absolute; overflow: hidden; }
  .panel > svg { position: absolute; inset: 0; width: 100%; height: 100%; }
  .panel .txt { position: absolute; color: var(--white); text-transform: uppercase; }

  /* Side panel */
  .side-panel { left: 40px; top: 90px; width: 1120px; height: 370px; }
  .side-panel .slogan {
    left: 20px; top: 40px; width: 330px; text-align: center;
    font-weight: 800; font-size: 38px; line-height: 1.2;
  }
  .slogan .accent { color: var(--teal); }
  .side-panel .brand-name {
    left: 395px; top: 70px; width: 340px; text-align: center;
    color: var(--blue); font-weight: 800; font-size: 58px; line-height: 1.05;
  }
  .brand-dot {
    display: block; width: 22px; height: 22px; border-radius: 50%;
    background: var(--orange); margin: 0 auto 12px;
  }
  .side-panel .discount {
    left: 790px; top: 200px; width: 320px; text-align: center;
    font-weight: 700; font-size: 17px; letter-spacing: 1.5px; line-height: 1.35;
  }
  .side-panel .phone {
    left: 60px; top: 303px; font-weight: 800; font-size: 52px; letter-spacing: 2px;
  }
  .side-panel .web {
    right: 30px; top: 312px; font-weight: 700; font-size: 36px;
    text-transform: none; letter-spacing: 1px;
  }

  /* Rear panel */
  .rear-panel { left: 375px; top: 530px; width: 450px; height: 600px; }
  .rear-panel .brand-name {
    left: 28px; top: 70px; width: 200px; text-align: center;
    color: var(--white); font-weight: 800; font-size: 34px; line-height: 1.1;
  }
  .rear-panel .brand-dot { background: var(--blue); }
  .rear-panel .slogan {
    left: 235px; top: 80px; width: 195px; text-align: center;
    font-weight: 800; font-size: 26px; line-height: 1.25;
  }
  .rear-panel .slogan .accent { color: var(--blue); }
  .rear-panel .discount {
    left: 30px; top: 300px; width: 390px; text-align: center;
    font-weight: 700; font-size: 16px; letter-spacing: 1.2px; line-height: 1.4;
  }
  .rear-panel .phone {
    left: 0; width: 450px; top: 370px; text-align: center;
    font-weight: 800; font-size: 50px; letter-spacing: 2px;
  }
  .rear-panel .web {
    left: 0; width: 450px; top: 488px; text-align: center;
    font-weight: 700; font-size: 28px; text-transform: none; letter-spacing: 1px;
  }
</style>
</head>
<body>

<section class="panel side-panel" aria-label="Truck side wrap">
  <svg viewBox="0 0 1120 370" preserveAspectRatio="none">
    <rect width="1120" height="370" fill="var(--off-white)"/>
    <polygon points="0,0 505,0 246,300 0,300" fill="var(--blue)"/>
    <polygon points="255,300 514,0 526,0 267,300" fill="var(--teal)"/>
    <polygon points="885,0 1120,0 1120,300 640,300" fill="var(--orange)"/>
    <rect y="300" width="1120" height="70" fill="var(--teal)"/>
  </svg>
  <div class="txt slogan">Keystone<br><span class="accent">Quality</span><br>Guaranteed</div>
  <div class="txt brand-name"><span class="brand-dot"></span>Keystone<br>Plumbing</div>
  <div class="txt discount">Military and First Responder<br>Discounts</div>
  <div class="txt phone">555-872-3096</div>
  <div class="txt web">www.keystoneplumb.com</div>
</section>

<section class="panel rear-panel" aria-label="Truck rear wrap">
  <svg viewBox="0 0 450 600" preserveAspectRatio="none">
    <rect width="450" height="600" fill="var(--off-white)"/>
    <rect x="10" y="10" width="430" height="460" fill="var(--orange)"/>
    <rect x="10" y="470" width="430" height="110" fill="var(--teal)"/>
  </svg>
  <div class="txt brand-name"><span class="brand-dot"></span>Keystone<br>Plumbing</div>
  <div class="txt slogan">Keystone<br><span class="accent">Quality</span><br>Guaranteed</div>
  <div class="txt discount">Military and First Responder<br>Discounts</div>
  <div class="txt phone">555-872-3096</div>
  <div class="txt web">www.keystoneplumb.com</div>
</section>

</body>
</html>
```